Web Design Project for Wren Nectar

We are a Honey Packing Company called Wren Nectar.
We need a new website.
We are open to many ideas.
We want to have headings like: Home/Products/About Us/Contact Us
We want an easy and uncomplicated website.
We need our logo attached to the center top or left top of the webpage.
We want to have a number of our products on the first page that increase in size once the cursor is placed on them.
We want to be able to add photos and products in the future as we expand.
Updates
Target Market(s)
Public
Food Distributors
Importers/Exporters
Industry/Entity Type
It Company
Look and feel
Each slider illustrates characteristics of the customer's brand and the style your logo design should communicate.

```html
<!DOCTYPE html>
<html lang="en">
<head>
<meta charset="utf-8">
<title>Wren Nectar</title>
<link rel="stylesheet" href="https://fonts.googleapis.com/css2?family=Abril+Fatface&family=Carlito&display=swap">
<style>
  :root {
    --gold: #b8852a;
    --gold-deep: #a87620;
    --gold-shade: #9e7022;
    --paper: #fdfdfd;
    --ink: #111111;
    --honey-dark: #a8420a;
    --honey: #e07a1a;
    --honey-light: #f2b04a;
    --studio-grey: #b9b9b9;
  }
  * { box-sizing: border-box; margin: 0; padding: 0; }
  html, body { width: 1200px; height: 1200px; overflow: hidden; background: var(--paper); }
  .page { position: relative; width: 1200px; height: 1200px; background: var(--paper); font-family: "Carlito", sans-serif; color: var(--ink); }

  .site-header { position: absolute; left: 0; top: 0; width: 1200px; height: 184px; background: var(--gold); }
  .band-ornament { position: absolute; border-radius: 40px; background: linear-gradient(180deg, rgba(158,112,34,0) 0%, rgba(158,112,34,0.55) 50%, rgba(158,112,34,0) 100%); }
  .band-ornament--header { left: 215px; top: 22px; width: 825px; height: 78px; }
  .band-ornament--footer { left: 170px; top: 16px; width: 860px; height: 46px; }

  .mascot-art { position: absolute; left: 73px; top: 47px; width: 147px; height: 164px; border-radius: 45%; background: radial-gradient(circle at 50% 40%, #e6e0e0 0%, #8d8080 55%, #1a1414 100%); }
  .bee-art { position: absolute; border-radius: 50%; background: radial-gradient(ellipse at 50% 50%, #e09a30 0%, #7a4a14 55%, rgba(60,40,10,0.6) 100%); }
  .bee-art--header { left: 976px; top: 107px; width: 151px; height: 100px; }
  .bee-art--footer { left: 1024px; top: 1127px; width: 86px; height: 62px; }
  .brand-name { position: absolute; left: 360px; top: 104px; width: 480px; text-align: center; font-family: "Abril Fatface", serif; font-size: 58px; line-height: 1; color: var(--ink); }

  .product-strip { position: absolute; left: 0; top: 251px; width: 1200px; height: 202px; background: var(--gold); }
  .product-photo { position: absolute; top: 4px; height: 194px; }
  .product-photo--spoon { left: 5px; width: 292px; background: radial-gradient(ellipse at 40% 55%, var(--honey-light) 0%, var(--honey) 40%, var(--honey-dark) 75%, #ffffff 100%); }
  .product-photo--squeeze { left: 307px; width: 293px; background: linear-gradient(180deg, var(--studio-grey) 0%, #c9a050 45%, #d08a20 75%, #e6e6e6 100%); }
  .product-photo--jar { left: 610px; width: 287px; background: radial-gradient(ellipse at 50% 55%, #e39a2a 0%, #c88a30 30%, #b5b5b5 60%, #c8c8c8 100%); }
  .product-photo--tub { left: 905px; width: 290px; background: radial-gradient(ellipse at 50% 55%, #d8561a 0%, #e07a20 35%, #b0aeb0 70%, #c4c4c4 100%); }

  .main-nav { position: absolute; left: 44px; top: 489px; width: 243px; }
  .nav-item { display: block; height: 58px; margin-bottom: 7px; padding: 14px 0 0 32px; background: linear-gradient(180deg, var(--gold-deep) 0%, #c49540 45%, #fbf6ec 100%); border-top: 1px solid #8a6018; font-family: "Abril Fatface", serif; font-size: 22px; line-height: 1.1; letter-spacing: 1.5px; color: var(--ink); text-decoration: none; }

  .welcome { position: absolute; left: 407px; top: 493px; width: 592px; }
  .welcome-title { font-family: "Abril Fatface", serif; font-weight: 400; font-size: 25px; letter-spacing: 2.5px; line-height: 1.2; }
  .welcome-text { margin-top: 44px; font-size: 20.8px; line-height: 25.4px; }

  .site-footer { position: absolute; left: 0; top: 1115px; width: 1200px; height: 85px; background: var(--gold); }
</style>
</head>
<body>
<div class="page">
  <header class="site-header">
    <div class="band-ornament band-ornament--header" role="img" aria-label="Decorative swirl ornament"></div>
    <div class="mascot-art" role="img" aria-label="Panda mascot illustration"></div>
    <div class="brand-name">Wren Nectar</div>
    <div class="bee-art bee-art--header" role="img" aria-label="Photo of a honey bee in flight"></div>
  </header>

  <section class="product-strip" aria-label="Products">
    <div class="product-photo product-photo--spoon" role="img" aria-label="Honey dipper in a jar of honey"></div>
    <div class="product-photo product-photo--squeeze" role="img" aria-label="Three squeeze bottles of honey in different sizes"></div>
    <div class="product-photo product-photo--jar" role="img" aria-label="Jar of honey with yellow lid"></div>
    <div class="product-photo product-photo--tub" role="img" aria-label="Large tub of honey with orange lid"></div>
  </section>

  <nav class="main-nav">
    <a class="nav-item" href="#">HOME</a>
    <a class="nav-item" href="#">PRODUCTS</a>
    <a class="nav-item" href="#">ABOUT US</a>
    <a class="nav-item" href="#">CONTACT US</a>
  </nav>

  <main class="welcome">
    <h1 class="welcome-title">Welcome to Wren Nectar</h1>
    <p class="welcome-text">Text for front page Text for front page Text for front page Text for front page Text for front page Text for front page Text for front page Text for front page Text for front page Text for front page Text for front page Text for front page Text for front page Text for front page Text for front page Text for front page Text for front page Text for front page Text for front page Text for front page Text for front page Text for front page Text for front page Text for front page Text for front page Text for front page Text for front page Text for front page Text for front page Text for front page Text for front page Text for front page Text for front page Text for front page Text for front page Text for front page Text for front page Text for front page Text for front page Text for front page Text for front page Text for front page</p>
  </main>

  <footer class="site-footer">
    <div class="band-ornament band-ornament--footer" role="img" aria-label="Decorative swirl ornament"></div>
  </footer>
  <div class="bee-art bee-art--footer" role="img" aria-label="Photo of a honey bee"></div>
</div>
</body>
</html>
```